Re-drawing and gpahically, according to coorporate design

Three flowcharts need to be re-drawn and graphically improved according to coorporate design

```html
<!DOCTYPE html>
<html lang="en">
<head>
<meta charset="utf-8">
<title>Circular Bioeconomy</title>
<link href="https://fonts.googleapis.com/css2?family=Open+Sans:wght@400;600;700;800&display=swap" rel="stylesheet">
<style>
  :root{
    --olive:#b5b00c;
    --olive-dark:#8f8a08;
    --teal:#587b7a;
    --teal-dark:#44625f;
    --green:#889c3c;
    --gray:#7f7f84;
    --gray-dark:#5e5e62;
    --chevron:#c9c46a;
    --ink:#1b1b1b;
    --white:#ffffff;
  }
  *{margin:0;padding:0;box-sizing:border-box}
  html,body{width:985px;height:1200px;overflow:hidden;background:var(--white)}
  body{font-family:"Open Sans",Arial,sans-serif;color:var(--ink)}
  .canvas{position:relative;width:985px;height:1200px;overflow:hidden}
  .brand{position:absolute;left:87px;top:104px;display:flex;align-items:center;gap:16px}
  .brand-mark{width:44px;height:44px;border-radius:50%;background:var(--teal);flex:none}
  .brand-name{font-weight:700;font-size:32px;line-height:1;color:var(--ink);white-space:nowrap}
  .title-band{position:absolute;left:55px;top:240px;width:876px;height:107px;background:var(--teal);display:flex;align-items:center;justify-content:center}
  .title-band h1{color:var(--white);font-weight:800;font-size:65px;letter-spacing:1px;line-height:1}
  .diagram{position:absolute;left:0;top:0;width:985px;height:1200px}
  .footer-band{position:absolute;left:0;top:1082px;width:985px;height:118px;background:var(--green)}
  .lbl{font-family:"Open Sans",Arial,sans-serif;font-weight:700;fill:var(--white);text-anchor:middle}
  .small{font-family:"Open Sans",Arial,sans-serif;font-size:8.5px;fill:var(--white)}
  .small-dark{font-family:"Open Sans",Arial,sans-serif;font-size:8.5px;fill:#555}
  .panel-head{font-family:"Open Sans",Arial,sans-serif;font-weight:700;font-size:11px;fill:var(--white)}
  .legend-lbl{font-family:"Open Sans",Arial,sans-serif;font-weight:700;font-size:8.5px;fill:var(--ink);text-anchor:middle}
  .ln-teal{fill:none;stroke:var(--teal);stroke-width:2.5}
  .ln-gray{fill:none;stroke:var(--gray);stroke-width:2.5}
  .ln-green{fill:none;stroke:var(--green);stroke-width:2.5}
</style>
</head>
<body>
<div class="canvas">
  <div class="brand">
    <span class="brand-mark"></span>
    <span class="brand-name">Halden Bioresource Lab</span>
  </div>

  <div class="title-band"><h1>CIRCULAR BIOECONOMY</h1></div>

  <svg class="diagram" viewBox="0 0 1500 1828" xmlns="http://www.w3.org/2000/svg" aria-label="Circular bioeconomy flowchart">
    <defs>
      <marker id="arr-teal" viewBox="0 0 10 10" refX="8" refY="5" markerWidth="6" markerHeight="6" orient="auto"><path d="M0 0 L10 5 L0 10 z" fill="#587b7a"/></marker>
      <marker id="arr-gray" viewBox="0 0 10 10" refX="8" refY="5" markerWidth="6" markerHeight="6" orient="auto"><path d="M0 0 L10 5 L0 10 z" fill="#7f7f84"/></marker>
      <marker id="arr-green" viewBox="0 0 10 10" refX="8" refY="5" markerWidth="6" markerHeight="6" orient="auto"><path d="M0 0 L10 5 L0 10 z" fill="#889c3c"/></marker>
    </defs>

    <g class="main-band">
      <rect x="190" y="1045" width="1100" height="24" fill="var(--olive)"/>
      <g fill="var(--chevron)">
        <path d="M258 1045h14l12 12-12 12h-14l12-12z"/><path d="M276 1045h14l12 12-12 12h-14l12-12z"/><path d="M294 1045h14l12 12-12 12h-14l12-12z"/>
        <path d="M710 1045h14l12 12-12 12h-14l12-12z"/><path d="M728 1045h14l12 12-12 12h-14l12-12z"/><path d="M746 1045h14l12 12-12 12h-14l12-12z"/>
        <path d="M1166 1045h14l12 12-12 12h-14l12-12z"/><path d="M1184 1045h14l12 12-12 12h-14l12-12z"/><path d="M1202 1045h14l12 12-12 12h-14l12-12z"/>
      </g>
    </g>

    <g class="connectors">
      <path class="ln-teal" d="M230 1034 H380 C440 1034 460 958 508 958" />
      <path class="ln-teal" d="M445 1000 L415 1025" marker-end="url(#arr-teal)"/>
      <path class="ln-teal" d="M852 882 C800 895 790 958 735 958 H675" marker-end="url(#arr-teal)"/>
      <path class="ln-teal" d="M730 958 H612"/>
      <path class="ln-teal" d="M558 976 V1004" marker-end="url(#arr-teal)"/>
      <path class="ln-teal" d="M230 1078 H380 C440 1078 460 1155 508 1155"/>
      <path class="ln-teal" d="M400 1078 L420 1079" marker-end="url(#arr-teal)"/>
      <path class="ln-teal" d="M558 1140 V1108" marker-end="url(#arr-teal)"/>
      <path class="ln-teal" d="M608 1150 C660 1135 680 1078 730 1078 H890"/>
      <path class="ln-teal" d="M700 1095 L722 1080" marker-end="url(#arr-teal)"/>
      <path class="ln-teal" d="M1250 1078 H1215 Q1193 1078 1193 1100 V1465 Q1193 1490 1168 1490 H752 Q727 1490 727 1465 V1185 Q727 1162 700 1162 H610"/>
      <path class="ln-teal" d="M1193 1280 V1300" marker-end="url(#arr-teal)"/>
      <path class="ln-teal" d="M1090 1490 H1072" marker-end="url(#arr-teal)"/>
      <path class="ln-teal" d="M727 1330 V1312" marker-end="url(#arr-teal)"/>
      <path class="ln-teal" d="M1094 872 H1013" marker-end="url(#arr-teal)"/>
      <path class="ln-teal" d="M1139 915 V1010 Q1139 1034 1115 1034 H966"/>
      <path class="ln-teal" d="M882 903 V914 H968 V903 M924 914 V933"/>
      <path class="ln-teal" d="M924 971 V1002" marker-end="url(#arr-teal)"/>
      <path class="ln-teal" d="M1106 1290 V1320 Q1106 1342 1084 1342 H977" marker-end="url(#arr-teal)"/>

      <path class="ln-gray" d="M187 1100 V1125 Q190 1150 230 1170 L338 1218"/>
      <path class="ln-gray" d="M260 1183 L278 1192" marker-end="url(#arr-gray)"/>
      <path class="ln-gray" d="M890 1090 H730 C660 1090 640 1221 540 1221 H495" marker-end="url(#arr-gray)"/>
      <path class="ln-gray" d="M540 1221 H438"/>
      <path class="ln-gray" d="M968 1056 H1090 Q1106 1056 1106 1075 V1140" marker-end="url(#arr-gray)"/>
      <path class="ln-gray" d="M924 1101 V1190" marker-end="url(#arr-gray)"/>
      <path class="ln-gray" d="M845 1190 V1160 H1002 V1190" />
      <path class="ln-gray" d="M845 1175 V1192" marker-end="url(#arr-gray)"/>
      <path class="ln-gray" d="M1002 1175 V1192" marker-end="url(#arr-gray)"/>
      <path class="ln-gray" d="M843 1256 V1282 H893 Q904 1290 906 1307" marker-end="url(#arr-gray)"/>
      <path class="ln-gray" d="M922 1256 V1307" marker-end="url(#arr-gray)"/>
      <path class="ln-gray" d="M1002 1256 V1282 H952 Q941 1290 939 1307" marker-end="url(#arr-gray)"/>

      <path class="ln-green" d="M923 1367 V1394 H843 V1425" marker-end="url(#arr-green)"/>
      <path class="ln-green" d="M923 1394 H1001 V1425" marker-end="url(#arr-green)"/>

      <g fill="#d6d3a8">
        <path d="M1096 1250 l10 10 10-10 v8 l-10 10 -10-10z"/>
        <path d="M1096 1264 l10 10 10-10 v8 l-10 10 -10-10z"/>
        <path d="M1096 1278 l10 10 10-10 v8 l-10 10 -10-10z"/>
      </g>
    </g>

    <g class="nodes">
      <circle cx="187" cy="1056" r="46" fill="var(--olive)"/><circle cx="187" cy="1056" r="41" fill="none" stroke="var(--olive-dark)" stroke-width="2"/>
      <text class="lbl" x="187" y="1053" font-size="13">Agriculture</text><text class="lbl" x="187" y="1068" font-size="13">&amp; Forestry</text>

      <circle cx="556" cy="1056" r="46" fill="var(--olive)"/><circle cx="556" cy="1056" r="41" fill="none" stroke="var(--olive-dark)" stroke-width="2"/>
      <text class="lbl" x="556" y="1061" font-size="13">Biomass</text>

      <circle cx="924" cy="1056" r="46" fill="var(--gray)"/><circle cx="924" cy="1056" r="41" fill="none" stroke="var(--white)" stroke-width="2"/>
      <text class="lbl" x="924" y="1061" font-size="13">Processing</text>

      <circle cx="1292" cy="1053" r="46" fill="var(--olive)"/><circle cx="1292" cy="1053" r="41" fill="none" stroke="var(--olive-dark)" stroke-width="2"/>
      <text class="lbl" x="1292" y="1045" font-size="12">Food</text><text class="lbl" x="1292" y="1059" font-size="12">&amp;</text><text class="lbl" x="1292" y="1074" font-size="12">Feed</text>

      <circle cx="387" cy="1221" r="49" fill="var(--gray)"/><circle cx="387" cy="1221" r="44" fill="none" stroke="var(--white)" stroke-width="2"/>
      <text class="lbl" x="387" y="1226" font-size="14">Residues</text>

      <circle cx="1138" cy="872" r="42" fill="var(--olive)"/><circle cx="1138" cy="872" r="37" fill="none" stroke="var(--olive-dark)" stroke-width="2"/>
      <text class="lbl" x="1138" y="870" font-size="9.5">Chemicals</text><text class="lbl" x="1138" y="882" font-size="9.5">&amp; Materials</text>

      <circle cx="884" cy="869" r="34" fill="var(--olive)"/><circle cx="884" cy="869" r="30" fill="none" stroke="var(--olive-dark)" stroke-width="1.5"/>
      <text class="lbl" x="884" y="857" font-size="8">Share</text><text class="lbl" x="884" y="866" font-size="8">maintain</text><text class="lbl" x="884" y="875" font-size="8">reuse</text><text class="lbl" x="884" y="884" font-size="8">redistribute</text>

      <circle cx="962" cy="869" r="34" fill="var(--olive)"/><circle cx="962" cy="869" r="30" fill="none" stroke="var(--olive-dark)" stroke-width="1.5"/>
      <text class="lbl" x="962" y="866" font-size="8">Bio-based</text><text class="lbl" x="962" y="877" font-size="8">products</text>

      <circle cx="1106" cy="1185" r="33" fill="var(--olive)"/><circle cx="1106" cy="1185" r="29" fill="none" stroke="var(--olive-dark)" stroke-width="1.5"/>
      <text class="lbl" x="1106" y="1184" font-size="8">Bioenergy</text><text class="lbl" x="1106" y="1194" font-size="8">&amp; Biofuels</text>

      <circle cx="923" cy="1340" r="27" fill="var(--green)"/><circle cx="923" cy="1340" r="23" fill="none" stroke="var(--white)" stroke-width="1.5"/>
      <text class="lbl" x="923" y="1344" font-size="11">CO₂</text>
    </g>

    <g class="boxes">
      <rect x="508" y="941" width="100" height="34" fill="var(--teal)"/>
      <text class="lbl" x="558" y="955" font-size="12">Organic</text><text class="lbl" x="558" y="970" font-size="12">Recycling</text>
      <rect x="508" y="1141" width="100" height="34" fill="var(--teal)"/>
      <text class="lbl" x="558" y="1155" font-size="12">Organic</text><text class="lbl" x="558" y="1170" font-size="12">Recycling</text>
      <rect x="877" y="933" width="95" height="38" fill="var(--teal)"/>
      <text class="lbl" x="924" y="945" font-size="8.5">Cascading</text><text class="lbl" x="924" y="955" font-size="8.5">Remanufacture</text><text class="lbl" x="924" y="965" font-size="8.5">Recycling</text>

      <rect x="811" y="1201" width="66" height="54" rx="4" fill="var(--gray)"/>
      <text class="lbl" x="844" y="1225" font-size="7.5">Anaerobic</text><text class="lbl" x="844" y="1234" font-size="7.5">Digestion</text>
      <rect x="894" y="1201" width="59" height="54" rx="4" fill="var(--gray)"/>
      <text class="lbl" x="923" y="1226" font-size="7.5">Biomass</text><text class="lbl" x="923" y="1235" font-size="7.5">Gastification</text>
      <rect x="971" y="1201" width="64" height="54" rx="4" fill="var(--gray)"/>
      <text class="lbl" x="1003" y="1229" font-size="7.5">Fermentation</text>

      <rect x="811" y="1434" width="68" height="27" rx="3" fill="var(--green)"/>
      <text class="lbl" x="845" y="1450" font-size="7.5">Power-To-Gas</text>
      <rect x="967" y="1434" width="68" height="27" rx="3" fill="var(--green)"/>
      <text class="lbl" x="1001" y="1446" font-size="7.5">Chemical</text><text class="lbl" x="1001" y="1455" font-size="7.5">Production</text>
    </g>

    <g class="panel panel-agriculture">
      <rect x="104" y="676" width="190" height="266" rx="8" fill="var(--teal)"/>
      <text class="panel-head" x="118" y="700">BioInnovation</text>
      <text class="panel-head" x="118" y="713">Agriculture &amp; Forestry</text>
      <text class="panel-head" x="118" y="726">Smart Farming</text>
      <line x1="118" y1="741" x2="270" y2="741" stroke="var(--white)" stroke-width="1"/>
      <text class="small" x="116" y="766">•  Precision Agriculture</text>
      <text class="small" x="116" y="777">•  Internet Of Farm Things</text>
      <text class="small" x="116" y="788">•  Robotics And Automation</text>
      <text class="small" x="116" y="799">•  Artificial Intelligence</text>
      <text class="small" x="116" y="810">•  Soil Nutrient Supply</text>
      <text class="small" x="116" y="821">•  Soil Sensors, Plant Sensors,</text>
      <text class="small" x="124" y="832">And Animal Sensors</text>
      <text class="small" x="116" y="843">•  Low Cost Genotyping, Gene Editing</text>
      <text class="small" x="116" y="854">•  Next Generation Breeding</text>
      <text class="small" x="116" y="865">•  Microbiota In Livestock</text>
      <text class="small" x="124" y="876">And Environment</text>
      <text class="small" x="116" y="887">•  Higher Conversion Efficiency:</text>
      <text class="small" x="116" y="898">•  Increase Output While Reducing</text>
      <text class="small" x="124" y="909">Impact On The Environment</text>
      <text class="small" x="116" y="920">•  Sustainable Intensification</text>
    </g>

    <g class="panel panel-products">
      <rect x="882" y="680" width="153" height="126" rx="6" fill="var(--white)" stroke="var(--olive)" stroke-width="3"/>
      <path d="M882 686 a6 6 0 0 1 6 -6 H1029 a6 6 0 0 1 6 6 V729 H882 Z" fill="var(--olive)"/>
      <text class="panel-head" x="899" y="702">BioInnovation</text>
      <text class="panel-head" x="899" y="715">Products</text>
      <text class="small-dark" x="899" y="749">•  New Functionality &amp;</text>
      <text class="small-dark" x="907" y="758">Properties</text>
      <text class="small-dark" x="899" y="768">•  More Nature Compatibles</text>
      <text class="small-dark" x="899" y="777">•  New Applications</text>
      <text class="small-dark" x="899" y="786">•  Less Toxicity</text>
    </g>

    <g class="panel panel-chemicals">
      <rect x="1222" y="816" width="169" height="126" rx="6" fill="var(--white)" stroke="var(--olive)" stroke-width="3"/>
      <path d="M1222 822 a6 6 0 0 1 6 -6 H1385 a6 6 0 0 1 6 6 V864 H1222 Z" fill="var(--olive)"/>
      <text class="panel-head" x="1238" y="836">BioInnovation</text>
      <text class="panel-head" x="1238" y="849">Chemicals</text>
      <text class="small-dark" x="1232" y="878">•  Innovation Molecules</text>
      <text class="small-dark" x="1232" y="888">•  New Chemicals And Materials</text>
      <text class="small-dark" x="1232" y="897">•  New Functionalities &amp; Properties</text>
      <text class="small-dark" x="1232" y="907">•  More Nature Compatible</text>
      <text class="small-dark" x="1232" y="917">•  Less Toxicity</text>
      <text class="small-dark" x="1232" y="926">•  Green And Sustainable Chemistry</text>
    </g>

    <g class="panel panel-food">
      <rect x="1239" y="1157" width="149" height="126" rx="6" fill="var(--white)" stroke="var(--olive)" stroke-width="3"/>
      <path d="M1239 1163 a6 6 0 0 1 6 -6 H1382 a6 6 0 0 1 6 6 V1205 H1239 Z" fill="var(--olive)"/>
      <text class="panel-head" x="1253" y="1182">BioInnovation</text>
      <text class="panel-head" x="1253" y="1195">Food &amp; Feed</text>
      <text class="small-dark" x="1251" y="1227">•  Food Quality And Safety</text>
      <text class="small-dark" x="1251" y="1237">•  Functional Food Ingredients</text>
      <text class="small-dark" x="1251" y="1246">•  Bioactive Phytochemicals</text>
      <text class="small-dark" x="1251" y="1256">•  Food Nutrients With New</text>
      <text class="small-dark" x="1259" y="1266">Functionality</text>
    </g>

    <g class="panel panel-processing">
      <rect x="1238" y="1331" width="151" height="165" rx="7" fill="var(--teal)"/>
      <text class="panel-head" x="1251" y="1358">BioInnovation</text>
      <text class="panel-head" x="1251" y="1371">Smart Processing</text>
      <line x1="1249" y1="1383" x2="1382" y2="1383" stroke="var(--white)" stroke-width="1"/>
      <text class="small" x="1250" y="1404">•  New Efficient, Short Pathways</text>
      <text class="small" x="1250" y="1414">•  Low Energy</text>
      <text class="small" x="1250" y="1423">•  Low Toxicities</text>
      <text class="small" x="1250" y="1433">•  Elimination Of Harsh Chemicals</text>
      <text class="small" x="1250" y="1443">•  Lower Temperature</text>
      <text class="small" x="1250" y="1452">•  Lower Pressure</text>
      <text class="small" x="1250" y="1462">•  From Oxidation To Reduction</text>
      <text class="small" x="1250" y="1472">•  High Efficiency</text>
      <text class="small" x="1250" y="1481">•  Synthetic Biology</text>
    </g>

    <g class="panel panel-bioeconomy">
      <rect x="108" y="1364" width="135" height="112" rx="5" fill="var(--teal)"/>
      <text class="panel-head" x="125" y="1389">Bioeconomy</text>
      <line x1="120" y1="1403" x2="231" y2="1403" stroke="var(--white)" stroke-width="1"/>
      <text class="small" x="120" y="1422">• Renewability</text>
      <text class="small" x="120" y="1431">• Saving fossil resources</text>
      <text class="small" x="120" y="1441">• Climate friendly</text>
      <text class="small" x="120" y="1450">• Improve productivity and</text>
      <text class="small" x="120" y="1460">• sustainability</text>
    </g>

    <g class="legend">
      <circle cx="376" cy="1406" r="33" fill="var(--olive)"/>
      <text class="legend-lbl" x="376" y="1461">BIOECONOMY</text>
      <circle cx="478" cy="1406" r="33" fill="var(--teal)"/>
      <text class="legend-lbl" x="478" y="1461">CIRCULAR</text><text class="legend-lbl" x="478" y="1470">ECONOMY</text>
      <circle cx="583" cy="1406" r="33" fill="var(--green)"/>
      <text class="legend-lbl" x="583" y="1461">CARBON</text><text class="legend-lbl" x="583" y="1470">CYCLE</text><text class="legend-lbl" x="583" y="1480">ECONOMY</text>
    </g>
  </svg>

  <div class="footer-band"></div>
</div>
</body>
</html>
```